One page sales fact sheet for data consultancy company

We need a serious and professional looking 1-page fact sheet that we want to send over to potential clients via email.
The upper part should consists of a header, the client logo and 3 charts.
(1 chart with 5 datapoints / 1 chart with 3 bubbles and percentage in it, 1 chart with numbers and text)
In the lower part there should be some text description about our company and a big chart consisting of a table (see drawing).
See attached drawing to get a better understanding of the whole idea.
The fact sheet should be catchy but professional in the same way.
Colors your choice but classic, i.e. black/white/grey/blue
The contest winner can expect more work from us based on the winning design.
*Please note that the logo reflects our original logo style but is not our
actual company name for privacy reasons

```html
<!DOCTYPE html>
<html lang="en">
<head>
<meta charset="utf-8">
<title>VORIN – Market Analysis Fact Sheet</title>
<link rel="stylesheet" href="https://fonts.googleapis.com/css2?family=Montserrat:wght@300;700;800&family=Raleway:wght@300;400&family=Open+Sans:wght@400&display=swap">
<style>
  :root {
    --navy: #212633;
    --navy-light: #2c3242;
    --navy-stripe: #272d3b;
    --white: #ffffff;
    --teal: #86dadd;
    --grey: #8b8e95;
    --backdrop: #dcdedd;
    --label-bg: #e6e7e9;
  }
  * { box-sizing: border-box; margin: 0; padding: 0; }
  html, body { width: 1200px; height: 1200px; overflow: hidden; }
  body {
    background: var(--backdrop);
    font-family: "Open Sans", Arial, sans-serif;
    color: var(--white);
    position: relative;
  }
  .sheet {
    position: absolute;
    left: 197px; top: 30px;
    width: 806px; height: 1140px;
    background: var(--navy);
    overflow: hidden;
  }
  .header-lines { position: absolute; left: 0; top: 0; }
  .brand {
    position: absolute; left: 0; width: 100%; top: 78px;
    padding-left: 150px;
    text-align: center;
    font-family: "Montserrat", sans-serif;
    font-weight: 800; font-size: 78px; letter-spacing: 2px;
  }
  .tracked {
    position: absolute;
    font-family: "Raleway", sans-serif; font-weight: 300;
    letter-spacing: 12px; text-transform: uppercase;
  }
  .title-market { top: 232px; left: 0; width: 100%; text-align: center; font-size: 22px; padding-left: 150px; }
  .bar-chart { position: absolute; left: 70px; top: 282px; }
  .divider-v { position: absolute; left: 435px; top: 300px; width: 2px; height: 165px; background: var(--white); }
  .title-types { top: 330px; left: 470px; font-size: 18px; letter-spacing: 10px; }
  .share {
    position: absolute; top: 382px; width: 98px; height: 50px;
    border: 1.5px solid var(--teal);
    transform: skewX(-20deg);
    display: flex; align-items: center; justify-content: center;
  }
  .share span {
    transform: skewX(20deg);
    font-family: "Montserrat", sans-serif; font-weight: 800; font-size: 28px;
  }
  .share small { font-size: 17px; }
  .stat { position: absolute; top: 478px; text-align: center; }
  .stat-number { font-family: "Montserrat", sans-serif; font-weight: 300; font-size: 54px; line-height: 1; }
  .stat-label {
    margin-top: 6px; display: inline-block;
    background: var(--label-bg); color: var(--navy);
    font-family: "Montserrat", sans-serif; font-weight: 800; font-size: 17px;
    padding: 2px 18px; transform: skewX(-20deg);
  }
  .stat-label span { display: inline-block; transform: skewX(20deg); }
  .sales-frame {
    position: absolute; left: 70px; top: 565px; width: 650px; height: 120px;
    border: 1.5px solid var(--white); transform: skewX(-20deg);
  }
  .sales-text {
    position: absolute; left: 0; width: 100%; top: 606px; text-align: center;
    font-family: "Montserrat", sans-serif; font-weight: 800; font-size: 40px;
  }
  .summary {
    position: absolute; left: 100px; width: 600px; top: 712px;
    text-align: center; font-size: 13.5px; line-height: 1.35;
  }
  .title-competitors { top: 832px; left: 0; width: 100%; text-align: center; font-size: 22px; }
  .layers { position: absolute; top: 888px; left: 40px; width: 726px; display: flex; justify-content: space-between; }
  .layer { font-family: "Montserrat", sans-serif; font-size: 13px; letter-spacing: 2px; text-transform: uppercase; width: 140px; }
  .layer-sep { width: 2px; height: 40px; background: var(--white); transform: skewX(-15deg); margin-top: 10px; }
  .levels { position: absolute; top: 960px; left: 60px; width: 600px; display: flex; gap: 50px; }
  .level { display: flex; align-items: center; gap: 10px; font-family: "Raleway", sans-serif; font-size: 16px; letter-spacing: 2px; }
  .footer-band { position: absolute; left: 0; bottom: 0; width: 100%; height: 78px; background: var(--white); }
</style>
</head>
<body>
<main class="sheet">
  <svg class="header-lines" width="806" height="220" viewBox="0 0 806 220">
    <rect x="0" y="14" width="806" height="7" fill="#fff"/>
    <line x1="300" y1="40" x2="806" y2="40" stroke="#fff" stroke-width="5"/>
    <line x1="300" y1="40" x2="150" y2="145" stroke="#fff" stroke-width="6"/>
    <line x1="0" y1="145" x2="150" y2="145" stroke="#fff" stroke-width="6"/>
    <rect x="0" y="200" width="806" height="8" fill="#fff"/>
  </svg>
  <div class="brand">VORIN</div>

  <h1 class="tracked title-market">Market Analysis</h1>

  <svg class="bar-chart" width="340" height="180" viewBox="0 0 340 180" role="img" aria-label="Bar chart of market data trending upward">
    <rect x="10" y="0" width="330" height="180" fill="#262c3a"/>
    <rect x="10" y="20" width="330" height="20" fill="#2e3445"/>
    <rect x="10" y="60" width="330" height="20" fill="#2e3445"/>
    <rect x="10" y="100" width="330" height="20" fill="#2e3445"/>
    <rect x="10" y="140" width="330" height="20" fill="#2e3445"/>
    <text x="110" y="42" fill="#fff" font-family="Raleway, sans-serif" font-weight="300" font-size="18" letter-spacing="8">DATA</text>
    <g>
      <rect x="14"  y="160" width="14" height="14" fill="#fff"/>
      <rect x="34"  y="150" width="14" height="24" fill="#86dadd"/>
      <rect x="54"  y="142" width="14" height="32" fill="#8b8e95"/>
      <rect x="74"  y="130" width="14" height="44" fill="#fff"/>
      <rect x="94"  y="124" width="14" height="50" fill="#86dadd"/>
      <rect x="114" y="116" width="14" height="58" fill="#8b8e95"/>
      <rect x="134" y="98"  width="14" height="76" fill="#fff"/>
      <rect x="154" y="88"  width="14" height="86" fill="#86dadd"/>
      <rect x="174" y="92"  width="14" height="82" fill="#fff"/>
      <rect x="194" y="80"  width="14" height="94" fill="#8b8e95"/>
      <rect x="214" y="62"  width="14" height="112" fill="#fff"/>
      <rect x="234" y="68"  width="14" height="106" fill="#86dadd"/>
      <rect x="254" y="50"  width="14" height="124" fill="#8b8e95"/>
      <rect x="274" y="44"  width="14" height="130" fill="#fff"/>
      <rect x="294" y="36"  width="14" height="138" fill="#86dadd"/>
      <rect x="314" y="20"  width="14" height="154" fill="#fff"/>
    </g>
  </svg>
  <div class="divider-v"></div>

  <h2 class="tracked title-types">Product Types</h2>
  <div class="share" style="left:462px"><span>40<small>%</small></span></div>
  <div class="share" style="left:572px"><span>30<small>%</small></span></div>
  <div class="share" style="left:682px"><span>20<small>%</small></span></div>

  <div class="sales-frame"></div>
  <div class="stat" style="left:75px;width:200px">
    <div class="stat-number">20</div>
    <div class="stat-label"><span>VENDORS</span></div>
  </div>
  <div class="stat" style="left:285px;width:200px">
    <div class="stat-number">150</div>
    <div class="stat-label"><span>PRODUCTS</span></div>
  </div>
  <div class="stat" style="left:490px;width:280px">
    <div class="stat-number">350,000</div>
    <div class="stat-label"><span>AVAILABLE ITEMS</span></div>
  </div>
  <div class="sales-text">40 MILLION IN SALES</div>

  <p class="summary">Lorem ipsum dolor sit amet, consectetuer adipiscing elit, sed diam nonummy nibh euismod tincidunt ut laoreet dolore magna aliquam erat volutpat. Ut wisi enim ad minim veniam, quis nostrud exerci tation ullamcorper suscipit lobortis nisl ut aliquip ex ea commodo consequat. Duis autem vel eum iriure dolor in hendrerit in vulputate velit esse molestie consequat, vel illum</p>

  <h2 class="tracked title-competitors">Competitors</h2>
  <div class="layers">
    <div class="layer">Layer 1</div>
    <div class="layer-sep"></div>
    <div class="layer">Layer 2</div>
    <div class="layer-sep"></div>
    <div class="layer">Layer 3</div>
    <div class="layer-sep"></div>
    <div class="layer">Layer 4</div>
  </div>
  <div class="levels">
    <div class="level">
      <svg width="30" height="30" viewBox="0 0 30 30" fill="none" stroke="#fff" stroke-width="1.5"><circle cx="15" cy="9" r="6"/><path d="M3 28c1-7 6-10 12-10s11 3 12 10"/></svg>
      User Level
    </div>
    <div class="level">
      <svg width="30" height="30" viewBox="0 0 30 30" fill="none" stroke="#fff" stroke-width="1.5"><path d="M4 24a12 12 0 1 1 22 0"/><line x1="15" y1="20" x2="21" y2="11"/><circle cx="15" cy="20" r="1.5"/></svg>
      Entity Level
    </div>
    <div class="level">
      <svg width="30" height="30" viewBox="0 0 30 30" fill="none" stroke="#fff" stroke-width="1.5"><rect x="3" y="3" width="20" height="22"/><line x1="7" y1="9" x2="19" y2="9"/><line x1="7" y1="14" x2="15" y2="14"/><line x1="7" y1="19" x2="13" y2="19"/><circle cx="22" cy="22" r="5" fill="#212633"/><circle cx="22" cy="22" r="1.5"/></svg>
      Personal Level
    </div>
  </div>

  <div class="footer-band"></div>
</main>
</body>
</html>
```